Flight school needs business cards!

We need a cool business card design for two flight school employees. The Chief Flight Instructor and the Manager. Put simply, we teach people how to fly. I would think it would be cool to have the front of the business card look like a pilot's license (US pilot certificate) and the backside has the logo and contact information.

Target Market(s)

Someone who wants to learn how to fly.

Industry/Entity Type

Aviation

Requirements
Must have
• The front of the business card should look like a United States pilot license, and it should read:

Your Name Here
Your Address Here

DOB and other personal information should be left plank.

Then under where it says
"Has been found to be properly qualified to exercise the privileges of
It should say Sport Pilot
Private Pilot
Commercial pilot

Basically, it is a way of saying what types of pilot licenses we can train someone for, and should be motivating for someone to have in their wallet. Something they don't want to throw away

```html
<!DOCTYPE html>
<html lang="en">
<head>
<meta charset="utf-8">
<title>Meridian Aviation Business Cards</title>
<link href="https://fonts.googleapis.com/css2?family=Open+Sans:wght@400;600;700;800&display=swap" rel="stylesheet">
<style>
  :root{
    --stage:#1d1e21;
    --navy-deep:#111527;
    --navy-mid:#13275a;
    --navy-glow:#1b3a7a;
    --signal-red:#e3202b;
    --white:#ffffff;
    --ink:#111111;
    --sage:#84ae9f;
    --mist:#b9c4d4;
  }
  *{box-sizing:border-box;margin:0;padding:0}
  html,body{width:1200px;height:780px;overflow:hidden}
  body{background:var(--stage);font-family:"Open Sans",sans-serif;position:relative}

  .card{position:absolute;top:235px;width:540px;height:310px;border-radius:24px;overflow:hidden}
  .card--contact{left:30px;background:var(--navy-deep);color:var(--white)}
  .card--license{left:630px;background:linear-gradient(30deg,var(--sage) 0%,#9db8b4 55%,var(--mist) 100%);color:var(--ink)}

  /* contact side */
  .hero-art{position:absolute;left:-130px;top:10px;width:300px;height:300px;border-radius:50%;
    background:radial-gradient(circle at 60% 40%,var(--navy-glow),var(--navy-mid) 60%,#0c1a40);
    box-shadow:0 0 0 7px var(--signal-red)}
  .brand{position:absolute;display:flex;align-items:center;gap:8px;font-weight:700;font-size:15px;letter-spacing:.06em;text-transform:uppercase}
  .card--contact .brand{right:28px;top:28px;color:var(--white)}
  .brand-dot{width:26px;height:26px;border-radius:50%;border:3px solid var(--signal-red);background:var(--white)}
  .contact-list{position:absolute;left:262px;top:125px;list-style:none}
  .contact-list li{display:flex;align-items:flex-start;gap:10px;font-size:14px;line-height:1.25;margin-bottom:10px}
  .contact-icon{flex:none;width:22px;height:22px;border:1.6px solid var(--signal-red);border-radius:50%;display:flex;align-items:center;justify-content:center}
  .contact-icon svg{width:12px;height:12px;fill:none;stroke:var(--signal-red);stroke-width:2;stroke-linecap:round;stroke-linejoin:round}

  /* license side */
  .license-watermark{position:absolute;left:170px;top:30px;width:300px;height:300px;border-radius:50%;
    background:radial-gradient(circle,rgba(255,255,255,.10),rgba(110,150,140,.25) 70%);border:5px solid rgba(230,240,240,.35)}
  .card--license .brand{right:24px;top:24px;color:var(--navy-deep);font-size:13px}
  .license-body{position:absolute;left:34px;top:62px;right:24px;font-weight:700}
  .holder-name{font-size:24px;font-weight:800;margin-left:46px;letter-spacing:.01em}
  .field{display:flex;font-size:13.5px;line-height:1.3}
  .field-num{width:46px;flex:none}
  .gap{height:14px}
  .ratings{display:flex;gap:24px;margin-top:16px;margin-left:46px;font-size:14px;text-transform:uppercase}
</style>
</head>
<body>

<section class="card card--contact">
  <div class="hero-art" role="img" aria-label="Illustration of a small high-wing airplane climbing through a starry night sky"></div>
  <div class="brand"><span class="brand-dot"></span>Meridian Aviation</div>
  <ul class="contact-list">
    <li><span class="contact-icon"><svg viewBox="0 0 24 24"><path d="M5 3h4l2 5-2.5 1.5a11 11 0 0 0 6 6L16 13l5 2v4a2 2 0 0 1-2 2A17 17 0 0 1 3 5a2 2 0 0 1 2-2z"/></svg></span>+123 456 7890</li>
    <li><span class="contact-icon"><svg viewBox="0 0 24 24"><rect x="3" y="5" width="18" height="14" rx="2"/><path d="M3 7l9 6 9-6"/></svg></span>youremailaddress@goes.here</li>
    <li><span class="contact-icon"><svg viewBox="0 0 24 24"><circle cx="12" cy="12" r="9"/><path d="M3 12h18M12 3a14 14 0 0 1 0 18M12 3a14 14 0 0 0 0 18"/></svg></span>www.yourwebaddress.com</li>
    <li><span class="contact-icon"><svg viewBox="0 0 24 24"><path d="M12 21s-7-6.5-7-12a7 7 0 0 1 14 0c0 5.5-7 12-7 12z"/><circle cx="12" cy="9" r="2.5"/></svg></span>41 Larkspur Ave.<br>Fairhaven, NY 11490</li>
  </ul>
</section>

<section class="card card--license">
  <div class="license-watermark" role="img" aria-label="Faint illustration of a small airplane inside a circle"></div>
  <div class="brand"><span class="brand-dot"></span>Meridian Aviation</div>
  <div class="license-body">
    <p class="holder-name">YOUR NAME HERE</p>
    <p class="field"><span class="field-num">I.</span>217 Windsock Lane</p>
    <p class="field"><span class="field-num">II.</span>Harbor Ridge, CA 90615</p>
    <div class="gap"></div>
    <p class="field"><span class="field-num">III.</span>CONTACT NO. - +123 456 7890</p>
    <p class="field"><span class="field-num">IV.</span>EMAIL- mailaddress@goes.here</p>
    <p class="field"><span class="field-num">V.</span>NATIONALITY- USA</p>
    <p class="field"><span class="field-num">VI.</span>D.O.B- 01/01/20000</p>
    <p class="field"><span class="field-num">VII.</span>HAS BEEN FOUND TO BE PROPERLY<br>QUALIFIED TO EXERCISE THE PRIVILEGES OF</p>
    <div class="ratings"><span>★ Sport Pilot</span><span>★ Private Pilot</span><span>★ Commercial Pilot</span></div>
  </div>
</section>

</body>
</html>
```